Moscato Wine Brand Graphic Design - see photos for reference and sizing guide

In need of a graphic design for our brand VELVET MUSE Pink Moscato with the following requirements:1. Lantawan Theme - it is a popular festival in Philippines that means "many faces" and is symbolized by creative masks with vibrant colours and designs.2. We want a Lantawan Design on our moscato bottle to represent women as Velvet Muses.3. The lantawan has to be bright,colourful, with pink,purple,musk,greys,small silver and gold stars or stripes glitter or sparkle accents to it.4. It has to have a WOW Factor, feel good label design that is aimed at Women 18yrs to 45yrs old.5. A sample is provided but feel free to play around and the most vibrant, new world design for VELVET MUSE Pink Moscato label Wins.

Target Market(s)

Women 18 to 45 yrs of age, Asian and Western Market

Font styles to use
Script

Colors

Designer to choose colors to be used in the design.

Requirements
Must have
• Bright,Bold and Vibrant Design that matches the label and it has to be a sophisticated Mask Design please refer to photo as a guide. Let your imagination run wild.
• Label Measurements: Front Label
• Width: 125mm
• Height:95mm
• Height from Base: 21mm
Nice to have
• Accents of sparkles and glitter with gold,silver,purple,pink hues or use your creativity to create a stunning mask design. The wine bottle is in Arctic Blue Sparkling Wine Bottle that makes the bottle look like light purple once the wine is in it so put it in consideration when making the label and background.

```html
<!DOCTYPE html>
<html lang="en">
<head>
<meta charset="utf-8">
<title>Velvet Muse Pink Moscato – Front Label</title>
<link rel="stylesheet" href="https://fonts.googleapis.com/css2?family=Great+Vibes&family=Poiret+One&family=Roboto:wght@300&display=swap">
<style>
  :root {
    --page-bg: #0a0a0c;
    --label-black: #141414;
    --label-edge: #222;
    --mask-pink: #d63c8e;
    --mask-purple: #8a5bc9;
    --mask-gold: #e8b320;
    --mask-silver: #9a9a9a;
    --type-light: #e6e6e6;
    --type-grey: #a9a9a9;
    --dot-grey: #8c8c8c;
  }
  * { margin: 0; padding: 0; box-sizing: border-box; }
  html, body {
    width: 1200px;
    height: 2467px;
    overflow: hidden;
    background: var(--page-bg);
  }
  .canvas {
    position: relative;
    width: 1200px;
    height: 2467px;
  }
  .front-label {
    position: absolute;
    left: 70px;
    top: 373px;
    width: 1060px;
    height: 1720px;
    background: linear-gradient(90deg, var(--label-edge) 0%, var(--label-black) 20%, var(--label-black) 80%, var(--label-edge) 100%);
  }
  .mask-artwork {
    position: absolute;
    left: 100px;
    top: 80px;
    width: 860px;
    height: 950px;
    background:
      radial-gradient(ellipse 30% 22% at 50% 78%, rgba(154,154,154,0.55), transparent 70%),
      radial-gradient(ellipse 18% 28% at 50% 42%, rgba(232,179,32,0.55), transparent 75%),
      radial-gradient(ellipse 50% 45% at 50% 48%, rgba(214,60,142,0.6), rgba(138,91,201,0.35) 60%, transparent 80%);
    border-radius: 50% 50% 45% 45% / 60% 60% 40% 40%;
  }
  .brand-name {
    position: absolute;
    left: 0;
    right: 0;
    top: 1040px;
    text-align: center;
    font-family: "Great Vibes", cursive;
    font-size: 200px;
    line-height: 1.2;
    white-space: nowrap;
    background: linear-gradient(90deg, var(--mask-purple) 0%, var(--mask-pink) 50%, var(--mask-gold) 100%);
    -webkit-background-clip: text;
    background-clip: text;
    color: transparent;
  }
  .variety {
    position: absolute;
    left: 40px;
    right: 40px;
    top: 1310px;
    display: flex;
    align-items: center;
    justify-content: center;
    gap: 28px;
  }
  .variety-rule {
    flex: 1;
    height: 0;
    border-top: 4px dotted var(--dot-grey);
  }
  .variety-name {
    font-family: "Poiret One", sans-serif;
    font-size: 76px;
    letter-spacing: 6px;
    color: var(--type-light);
    white-space: nowrap;
  }
  .bottle-facts {
    position: absolute;
    left: 0;
    right: 0;
    top: 1505px;
    text-align: center;
    font-family: "Roboto", sans-serif;
    font-weight: 300;
    font-size: 40px;
    line-height: 60px;
    letter-spacing: 3px;
    color: var(--type-grey);
  }
</style>
</head>
<body>
  <main class="canvas">
    <section class="front-label">
      <div class="mask-artwork" role="img" aria-label="Ornate festival mask illustration in pink, purple, gold and silver with dotted bead accents"></div>
      <h1 class="brand-name">Velvet Muse</h1>
      <div class="variety">
        <span class="variety-rule"></span>
        <span class="variety-name">PINK MOSCATO</span>
        <span class="variety-rule"></span>
      </div>
      <p class="bottle-facts">0.75L<br>13% ALC.</p>
    </section>
  </main>
</body>
</html>
```